Vero M.Q. - Diagnostic Ultrasound Flyer

About US
Vero M.Q. is a concierge ultrasound company that provides onsite or offsite diagnostic ultrasounds. We have over 14 years experience in sonography, business management, and customer service. We offer both the physician and patient flexibility, convenience, and access to timely services.

We provide ultrasounds for the following specialties:
Obstetrics/Gynecology
Abdominal
Small Parts
Vascular

Company Features:
1. Onsite or Offsite Scans
2. Images Available Immediately for Referring Physician and Patient
3. Flexible Options for Ultrasound Interpretation/Billing
4. Access to Interpreting Radiologist
5. Final Report Process - 1-2 Business Days/ 1 hour for STAT.
6. PACS Storage with Secure Access.

We need a place to add in our contact information (address, email, website, phone)

We already have a logo and would like to use it ( they are attached). We would the colors to match the logo colors....maybe lighter version of yellow and blue.

```html
<!DOCTYPE html>
<html lang="en">
<head>
<meta charset="utf-8">
<title>Vero M.Q. – Diagnostic Ultrasound Flyer</title>
<link href="https://fonts.googleapis.com/css2?family=Montserrat:wght@400;500;600;700;800&display=swap" rel="stylesheet">
<style>
  :root{
    --backdrop:#c9c9c9;
    --paper:#ffffff;
    --navy:#1f1fa0;
    --sun:#f8b527;
    --sun-soft:#fff3dc;
    --ink:#222230;
    --muted:#6a6a78;
    --photo-deep:#0f5a86;
    --photo-light:#39c4ec;
  }
  *{box-sizing:border-box;margin:0;padding:0}
  html,body{width:1200px;height:800px;overflow:hidden;background:var(--backdrop);font-family:"Montserrat",sans-serif;color:var(--ink)}
  .flyer{position:absolute;left:324px;top:10px;width:552px;height:780px;background:var(--paper);overflow:hidden;box-shadow:0 6px 24px rgba(0,0,0,.18)}
  .brand{position:absolute;left:34px;top:40px;font-weight:800;font-size:24px;letter-spacing:1px;color:var(--navy)}
  .hero-photo{position:absolute;left:292px;top:14px;width:244px;height:244px;border-radius:50%;border:3px solid var(--navy);
    background:radial-gradient(circle at 45% 45%,var(--photo-light),#1a8fc4 55%,var(--photo-deep))}
  .headline{position:absolute;left:34px;top:88px;width:260px;font-weight:800;font-size:18.5px;line-height:1.28;text-transform:uppercase}
  .headline .warm{color:var(--sun)}
  .headline .cool{color:var(--navy)}
  .rule{display:block;height:2px;background:var(--sun);margin-top:6px;width:255px}
  .about{position:absolute;left:34px;top:268px;width:250px}
  .section-title{font-weight:800;font-size:17px;color:var(--navy);text-transform:uppercase;letter-spacing:.5px}
  .about p{margin-top:8px;font-size:8.5px;line-height:1.55;color:var(--muted)}
  .features{position:absolute;left:34px;top:368px;width:260px}
  .feature-list{list-style:none;margin-top:16px}
  .feature-list li{display:flex;align-items:center;gap:12px;margin-bottom:14px;font-weight:700;font-size:9px;line-height:1.35;color:var(--ink)}
  .feature-icon{flex:0 0 28px;height:28px;border:1.6px solid var(--navy);border-radius:6px;background:#eef0ff}
  .specialties{position:absolute;left:300px;top:330px;width:230px}
  .spec-title{border-left:3px solid var(--sun);padding-left:9px;font-weight:800;font-size:12.5px;line-height:1.3;color:var(--navy);text-transform:uppercase}
  .spec-grid{display:grid;grid-template-columns:1fr 1fr;gap:22px 12px;margin-top:26px}
  .spec{display:flex;flex-direction:column;align-items:center;text-align:center;font-weight:800;font-size:11.5px;color:var(--ink)}
  .spec:nth-child(even){transform:translateY(-18px)}
  .spec-badge{width:56px;height:56px;border-radius:50%;border:2px dashed var(--navy);padding:6px;margin-bottom:8px}
  .spec-badge span{display:block;width:100%;height:100%;border-radius:50%;background:var(--sun-soft);border:1.5px solid var(--sun)}
  .contact-band{position:absolute;left:0;bottom:0;width:100%;height:52px;background:var(--sun);display:flex;align-items:center;justify-content:space-around;padding:0 18px;font-weight:600;font-size:9.5px;color:var(--ink)}
  .contact-item{display:flex;align-items:center;gap:7px}
  .divider{width:1.5px;height:20px;background:var(--ink)}
  .contact-item svg{width:15px;height:15px;fill:none;stroke:var(--ink);stroke-width:1.6}
</style>
</head>
<body>
<main class="flyer">
  <div class="brand">VERO M.Q.</div>
  <div class="hero-photo" role="img" aria-label="Medical technology photo of a clinician viewing digital body scan graphics"></div>

  <h1 class="headline">
    <span class="warm">We offer both the physician and patient flexibility, convenience,</span>
    <span class="cool"> and access to timely services.</span>
    <span class="rule"></span>
  </h1>

  <section class="about">
    <h2 class="section-title">About Us</h2>
    <p>Vero M.Q. is a concierge ultrasound company that provides onsite or offsite diagnostic ultrasounds. We have over 14 years experience in sonography, business management, and customer service.</p>
  </section>

  <section class="features">
    <h2 class="section-title">Company Features</h2>
    <ul class="feature-list">
      <li><span class="feature-icon" role="img" aria-label="Ultrasound machine icon"></span>Onsite or Offsite Scans</li>
      <li><span class="feature-icon" role="img" aria-label="Physician and patient icon"></span>Images Available Immediately for Referring Physician and Patient</li>
      <li><span class="feature-icon" role="img" aria-label="Monitor icon"></span>Flexible Options for Ultrasound Interpretation/Billing</li>
      <li><span class="feature-icon" role="img" aria-label="Radiologist icon"></span>Access to Interpreting Radiologist</li>
      <li><span class="feature-icon" role="img" aria-label="Report clipboard icon"></span>Final Report Process - 1-2 Business Days/ 1 hour for STAT.</li>
      <li><span class="feature-icon" role="img" aria-label="Secure storage building icon"></span>PACS Storage with Secure Access.</li>
    </ul>
  </section>

  <section class="specialties">
    <h2 class="spec-title">We provide ultrasound for the following specialties:</h2>
    <div class="spec-grid">
      <div class="spec"><div class="spec-badge"><span role="img" aria-label="Uterus and fetus icon"></span></div>Obstetrics<br>Gynecology</div>
      <div class="spec"><div class="spec-badge"><span role="img" aria-label="Intestines icon"></span></div>Abdominal</div>
      <div class="spec"><div class="spec-badge"><span role="img" aria-label="Digestive organs icon"></span></div>Small Parts</div>
      <div class="spec"><div class="spec-badge"><span role="img" aria-label="Heart and vessels icon"></span></div>Vascular</div>
    </div>
  </section>

  <footer class="contact-band">
    <div class="contact-item">
      <svg viewBox="0 0 16 16"><path d="M3 2h3l1 3-2 1.5a8 8 0 0 0 4.5 4.5L11 9l3 1v3a1 1 0 0 1-1 1A11 11 0 0 1 2 3a1 1 0 0 1 1-1z"/></svg>
      Ph no-555 014 2290
    </div>
    <span class="divider"></span>
    <div class="contact-item">
      <svg viewBox="0 0 16 16"><rect x="1.5" y="3.5" width="13" height="9"/><path d="M1.5 3.5 8 9l6.5-5.5"/></svg>
      Your email
    </div>
    <span class="divider"></span>
    <div class="contact-item">
      <svg viewBox="0 0 16 16"><circle cx="8" cy="8" r="6.5"/><ellipse cx="8" cy="8" rx="3" ry="6.5"/><path d="M1.5 8h13"/></svg>
      www.veromq-scan.com
    </div>
  </footer>
</main>
</body>
</html>
```